Design einer Frühjahrsbroschüre für Immobilienmakler
Zielgruppe
Wir sind Immobilienmakler und möchten eine neue Frühjahrsbroschüre verteilen lassen.
Wir haben über Gestaltwerkportal schon mehrere Projekte gemacht und waren immer zufrieden.
Unsere Zielgruppe sind Immobilienverkäufer.
Aufgabenstellung
Der Flyer soll die Größe haben DinA3 auf DinA4 gefaltet. Somit sind 4 DinA4 Seiten zu gestallten.
Bei Papier mit Schwung soll gedruckt werden. https://www.papier-mit-schwung.de/faltblatt-gefalzt-auf-din-a4-4seiter.html#content-view
1. Seite: Frühlingshaft und ansprechende Aufmachung. Harmonische Farben. Ein Slogan.
Frühjahrsaktion: Verkäufer erhält nach Verkauf als Dankeschön für den Auftrag und sein Vertrauen in uns einen neuen Kochfalke KF3 oder 1000€ in bar.
2. Immobilienverkauf in Coronazeiten.
Warum Verkaufen mit Nordhang-Immobilien Wendlacher
3. Aktuelle Immobilienangebote
4. Wir suchen für unsere Kunden
Im Anhang sind andere Flyer/Broschüren die uns seither gut gefallen haben.

```html
<!DOCTYPE html>
<html lang="de">
<head>
<meta charset="utf-8">
<title>Immobilienverkauf in Zeiten von Corona</title>
<link href="https://fonts.googleapis.com/css2?family=Anton&family=Ubuntu:wght@400&display=swap" rel="stylesheet">
<style>
  :root{
    --paper:#efefef;
    --paper-light:#f7f7f7;
    --ink:#1d5a6e;
    --teal-dark:#175c78;
    --teal:#128f86;
    --green:#14ad8e;
    --photo-dark:#5d6468;
    --photo-light:#c9cdcf;
  }
  *{margin:0;padding:0;box-sizing:border-box}
  html,body{width:1200px;height:600px;overflow:hidden;background:var(--paper)}
  .spread{position:relative;width:1200px;height:600px;background:var(--paper);overflow:hidden;
    font-family:"Ubuntu",sans-serif;color:var(--ink)}
  .backdrop{position:absolute;inset:0}
  .headline{position:absolute;left:0;width:720px;top:50px;text-align:center}
  .headline h1{font-family:"Anton",sans-serif;font-weight:400;font-size:23px;line-height:30px;
    letter-spacing:-0.4px;color:var(--ink);transform:scaleX(0.93)}
  .headline p{font-size:14px;line-height:16px;letter-spacing:0.3px;margin-top:0}
  .copy{position:absolute;font-size:12.2px;line-height:15.25px}
  .copy .para{margin-bottom:15.25px}
  .copy .line{display:block;white-space:nowrap}
  .copy .j{text-align:justify;text-align-last:justify;white-space:normal}
  .copy-left{left:160px;top:111px;width:403px}
  .copy-left .flow{text-align:justify}
  .copy-right{left:632px;top:324px}
  .year{position:absolute;left:1090px;top:518px;font-family:"Anton",sans-serif;font-size:45px;
    line-height:50px;color:#fff;letter-spacing:-0.5px}
</style>
</head>
<body>
<div class="spread">
  <svg class="backdrop" width="1200" height="600" viewBox="0 0 1200 600">
    <defs>
      <linearGradient id="tealLeft" x1="0" y1="0" x2="1" y2="1">
        <stop offset="0" stop-color="var(--teal-dark)"/>
        <stop offset="1" stop-color="var(--green)"/>
      </linearGradient>
      <linearGradient id="tealRight" x1="0" y1="1" x2="1" y2="0">
        <stop offset="0" stop-color="var(--teal)"/>
        <stop offset="1" stop-color="var(--green)"/>
      </linearGradient>
      <linearGradient id="photoTone" x1="0" y1="0" x2="1" y2="1">
        <stop offset="0" stop-color="var(--photo-dark)"/>
        <stop offset="0.5" stop-color="#8e9498"/>
        <stop offset="1" stop-color="var(--photo-light)"/>
      </linearGradient>
    </defs>
    <!-- soft light bands -->
    <polygon points="0,0 240,0 0,225" fill="var(--paper-light)"/>
    <polygon points="0,150 160,0 200,0 0,190" fill="#e6e6e6"/>
    <polygon points="900,330 1200,600 1130,600 870,360" fill="var(--paper-light)"/>
    <!-- photo area -->
    <polygon role="img" aria-label="Foto: Hand mit Hausmodell und Schlüssel vor Geschäftsanzug, dahinter weißes Hausmodell"
      points="600,0 1200,0 1200,370 1165,372 940,222 861,286 600,89" fill="url(#photoTone)"/>
    <polygon points="600,42 888,262 861,286 600,89" fill="var(--teal)" opacity="0.75"/>
    <polygon points="1020,0 1180,0 900,250 880,266" fill="var(--teal-dark)" opacity="0.25"/>
    <!-- left accent -->
    <polygon points="0,325 310,600 0,600" fill="url(#tealLeft)"/>
    <polygon points="0,430 190,600 110,600 0,505" fill="var(--teal-dark)" opacity="0.35"/>
    <!-- right accent -->
    <polygon points="1001,521 1200,341 1200,600 1087,600" fill="url(#tealRight)"/>
    <polygon points="1040,560 1200,400 1200,600 1087,600" fill="var(--teal-dark)" opacity="0.85"/>
  </svg>

  <header class="headline">
    <h1>IMMOBILIENVERKAUF IN ZEITEN VON CORONA</h1>
    <p>DIGITAL UND PERSÖNLICH</p>
  </header>

  <section class="copy copy-left">
    <p class="para flow">Sie fragen sich ob es gerade jetzt – mitten in der Corona-Krise – ein guter Zeitpunkt für den Immobilienverkauf ist? Wie kann man dies mit den aktuellen Corona-Vorschriften vereinbaren? Welcher Verkaufspreis lässt sich erzielen?</p>
    <p class="para flow">Diese und viele weitere Fragen beantworten wir Ihnen im Rahmen einer unverbindlichen Beratung. Gerne per Telefon oder Videokonferenz.<br>Ist Ihnen eine persönliche Beratung lieber?<br>Dann machen wir auch dies möglich wenn es gewährleistet ist dass man den Mindestabstand von 1,5m einhalten kann. Gerne halten wir die Gespräche auch im Freien wie im Garten oder auf dem Balkon ab. Natürlich kommen wir immer mit Mundschutz und Handschuhen.</p>
    <p class="para flow">Nach unserer Beratung und einer unverbindlichen und kostenlosen Objektbewertung haben Sie eine fundierte Grundlage um zu entscheiden ob ein Verkauf für Sie in Frage kommt.</p>
    <div class="para">
      <span class="line">Haben Sie sich zum Verkauf Ihrer Immobilie mit uns entscheiden</span>
      <span class="line j">machen wir ansprechende, professionelle Fotos und erstellen ein</span>
      <span class="line j" style="margin-left:3px">attraktives Exposé welche Sie per Mail vorab erhalten und freigeben</span>
      <span class="line j" style="margin-left:19px">können. Der Fototermin findet selbstverständlich auch unter</span>
      <span class="line" style="margin-left:35px">Einhaltung der Hygienemaßnahmen statt.</span>
      <span class="line j" style="margin-left:51px">Wir bewerben Ihre Immobilie auf Portalen wie</span>
      <span class="line" style="margin-left:67px">Wohnfinder24, Markthalle Kleinanzeigen, Nachbarnetz und auf</span>
      <span class="line" style="margin-left:85px">unserer Homepage.</span>
      <span class="line j" style="margin-left:99px">Darüber hinaus ermitteln wir passende</span>
      <span class="line" style="margin-left:115px">Kaufinteressenten aus unserer Datenbank.</span>
    </div>
  </section>

  <section class="copy copy-right">
    <div class="para" style="width:410px">
      <span class="line">Um Ihre Immobilie auch in diesen Zeiten erfolgreich zu verkaufen,</span>
      <span class="line j" style="width:376px">haben wir auch für Ihre Kaufinteressenten digitale Lösungen</span>
      <span class="line j" style="width:392px">geschaffen. Sollte ein Vor-Ort-Termin (mit max. 2 Personen) nicht</span>
      <span class="line j" style="width:412px">möglich sein, besteht auch hier die Möglichkeit Ihre Immobilie in</span>
      <span class="line">Videokonferenzen und Video-Besichtigungstouren zu präsentieren.</span>
    </div>
    <div class="para" style="width:441px">
      <span class="line j">Käufer und Kaufpreis passen für Sie? Dann kümmern wir uns um den</span>
      <span class="line j" style="width:424px">Kaufvertrag und den Notartermin, um den Verkauf rechtssicher</span>
      <span class="line">abzuschließen.</span>
    </div>
    <div class="para">
      <span class="line j" style="width:374px">Übrigens: In den letzten zwei Jahren waren 93 Prozent unserer</span>
      <span class="line">Kunden mit unserem Service, der Vermarktungsdauer und dem</span>
      <span class="line">erzielten Preis sehr zufrieden.</span>
    </div>
  </section>

  <div class="year">2020</div>
</div>
</body>
</html>
```